Business card for home developer

Name, email, phone #, logo, address, lic # and slogan.
Slogan to say something like, "Leader in quality neighborhood communities" maybe? The last one said "A sept above the rest". Some thing saying we are above the other people.
The card can be two sided?
Home buyers
Business

```html
<!DOCTYPE html>
<html lang="en">
<head>
<meta charset="utf-8">
<title>Summit Ridge Homes – Business Card</title>
<link rel="stylesheet" href="https://fonts.googleapis.com/css2?family=Arimo:wght@400;700&family=Lato:wght@400&display=swap">
<style>
  :root {
    --stage: #000000;
    --brick: #a82421;
    --brick-tint: #b9403c;
    --navy: #284784;
    --navy-tint: #3a5a96;
    --paper: #ffffff;
    --ink: #111111;
    --brick-soft: #f3dedd;
    --navy-soft: #dfe5f1;
  }
  * { box-sizing: border-box; margin: 0; padding: 0; }
  html, body { width: 1200px; height: 900px; overflow: hidden; }
  body { background: var(--stage); position: relative; font-family: "Arimo", Arial, sans-serif; }

  .card { position: absolute; overflow: hidden; }
  .card--front { color: var(--paper); }
  .card--back { background: var(--paper); color: var(--ink); }

  .card--red.card--front  { left: 15px; top: 26px; width: 622px; height: 364px; background: var(--brick); z-index: 4; }
  .card--red.card--back   { left: 15px; top: 390px; width: 622px; height: 363px; z-index: 3; }
  .card--blue.card--front { left: 637px; top: 113px; width: 563px; height: 378px; background: var(--navy); z-index: 1; }
  .card--blue.card--back  { left: 600px; top: 491px; width: 600px; height: 364px; z-index: 2; }

  .wordmark { position: absolute; display: flex; align-items: center; gap: 12px; font-family: "Arimo", Arial, sans-serif; font-weight: 700; line-height: 1; white-space: nowrap; z-index: 2; }
  .wordmark__dot { border-radius: 50%; flex: none; }
  .wordmark__name { display: flex; flex-direction: column; letter-spacing: 1px; }
  .wordmark__main { font-size: 1em; }
  .wordmark__sub { font-size: 0.42em; letter-spacing: 3px; margin-top: 8px; align-self: flex-end; }

  .wordmark--front { font-size: 50px; color: var(--paper); }
  .wordmark--front .wordmark__dot { width: 40px; height: 40px; background: var(--paper); }
  .wordmark--back { font-size: 30px; }
  .wordmark--back .wordmark__dot { width: 22px; height: 22px; }
  .card--red .wordmark--back { color: var(--brick); }
  .card--red .wordmark--back .wordmark__dot { background: var(--brick); }
  .card--blue .wordmark--back { color: var(--navy); }
  .card--blue .wordmark--back .wordmark__dot { background: var(--navy); }

  .roofline-band { position: absolute; left: 0; right: 0; height: 68px; z-index: 1; }
  .card--red.card--front .roofline-band { background: linear-gradient(var(--brick), var(--brick-tint)); }
  .card--blue.card--front .roofline-band { background: linear-gradient(var(--navy), var(--navy-tint)); }
  .card--red.card--back .roofline-band { background: var(--brick-soft); }
  .card--blue.card--back .roofline-band { background: var(--navy-soft); }

  .website { position: absolute; left: 0; right: 0; text-align: center; font-family: "Lato", Arial, sans-serif; font-size: 17px; letter-spacing: 0.3px; white-space: nowrap; }

  .person { position: absolute; font-family: "Arimo", Arial, sans-serif; font-size: 14px; line-height: 18px; color: var(--ink); white-space: nowrap; }
  .person__name { text-transform: uppercase; }

  .contact-icons { position: absolute; display: flex; flex-direction: column; gap: 5px; }
  .contact-icons svg { width: 13px; height: 14px; display: block; }
  .card--red .contact-icons { color: var(--brick); }
  .card--blue .contact-icons { color: var(--navy); }

  .slogan { position: absolute; left: 0; right: 0; text-align: center; font-family: "Lato", Arial, sans-serif; font-size: 14px; white-space: nowrap; }
  .card--red .slogan { color: var(--brick); }
  .card--blue .slogan { color: var(--navy); }
</style>
</head>
<body>

<section class="card card--blue card--front">
  <div class="wordmark wordmark--front" style="left:76px; top:124px;">
    <span class="wordmark__name"><span class="wordmark__main">SUMMIT RIDGE</span><span class="wordmark__sub">HOMES</span></span>
    <span class="wordmark__dot"></span>
  </div>
  <div class="roofline-band" role="img" aria-label="Row of house outlines" style="top:247px;"></div>
  <p class="website" style="top:326px; right:36px;">www.yourwebpage.com</p>
</section>

<section class="card card--blue card--back">
  <div class="wordmark wordmark--back" style="left:36px; top:28px;">
    <span class="wordmark__name"><span class="wordmark__main">SUMMIT RIDGE</span><span class="wordmark__sub">HOMES</span></span>
    <span class="wordmark__dot"></span>
  </div>
  <div class="person" style="left:36px; top:142px;">
    <p class="person__name">Your Name</p>
    <p class="person__role">Your position</p>
  </div>
  <div class="contact-icons" style="left:392px; top:147px;">
    <svg viewBox="0 0 14 14" aria-hidden="true"><path d="M3 1l3 3-1.5 1.5c.8 1.6 2 2.8 3.5 3.5L9.5 7.5l3 3L11 12.5C6 12 2 8 1.5 3z" fill="currentColor"/></svg>
    <svg viewBox="0 0 14 14" aria-hidden="true"><rect x="1.5" y="3.5" width="11" height="7" fill="none" stroke="currentColor" stroke-width="1.4"/><path d="M1.5 3.5L7 8l5.5-4.5" fill="none" stroke="currentColor" stroke-width="1.4"/></svg>
    <svg viewBox="0 0 14 14" aria-hidden="true"><circle cx="7" cy="7" r="5.5" fill="none" stroke="currentColor" stroke-width="1.3"/><ellipse cx="7" cy="7" rx="2.4" ry="5.5" fill="none" stroke="currentColor" stroke-width="1.1"/><path d="M1.5 7h11" stroke="currentColor" stroke-width="1.1"/></svg>
    <svg viewBox="0 0 14 14" aria-hidden="true"><path d="M7 13S2.5 8 2.5 5.3a4.5 4.5 0 019 0C11.5 8 7 13 7 13z" fill="none" stroke="currentColor" stroke-width="1.5"/><circle cx="7" cy="5.3" r="1.5" fill="currentColor"/></svg>
  </div>
  <div class="roofline-band" role="img" aria-label="Row of house outlines" style="top:247px;"></div>
  <p class="slogan" style="top:328px; padding-left:26px;">"Leader in quality neighborhood communities"</p>
</section>

<section class="card card--red card--front">
  <div class="wordmark wordmark--front" style="left:118px; top:100px;">
    <span class="wordmark__name"><span class="wordmark__main">SUMMIT RIDGE</span><span class="wordmark__sub">HOMES</span></span>
    <span class="wordmark__dot"></span>
  </div>
  <div class="roofline-band" role="img" aria-label="Row of house outlines" style="top:239px;"></div>
  <p class="website" style="top:320px;">www.yourwebpage.com</p>
</section>

<section class="card card--red card--back">
  <div class="wordmark wordmark--back" style="left:22px; top:42px;">
    <span class="wordmark__name"><span class="wordmark__main">SUMMIT RIDGE</span><span class="wordmark__sub">HOMES</span></span>
    <span class="wordmark__dot"></span>
  </div>
  <div class="person" style="left:22px; top:169px;">
    <p class="person__name">Your Name</p>
    <p class="person__role">Your position</p>
  </div>
  <div class="contact-icons" style="left:393px; top:145px;">
    <svg viewBox="0 0 14 14" aria-hidden="true"><path d="M3 1l3 3-1.5 1.5c.8 1.6 2 2.8 3.5 3.5L9.5 7.5l3 3L11 12.5C6 12 2 8 1.5 3z" fill="currentColor"/></svg>
    <svg viewBox="0 0 14 14" aria-hidden="true"><rect x="1.5" y="3.5" width="11" height="7" fill="none" stroke="currentColor" stroke-width="1.4"/><path d="M1.5 3.5L7 8l5.5-4.5" fill="none" stroke="currentColor" stroke-width="1.4"/></svg>
    <svg viewBox="0 0 14 14" aria-hidden="true"><circle cx="7" cy="7" r="5.5" fill="none" stroke="currentColor" stroke-width="1.3"/><ellipse cx="7" cy="7" rx="2.4" ry="5.5" fill="none" stroke="currentColor" stroke-width="1.1"/><path d="M1.5 7h11" stroke="currentColor" stroke-width="1.1"/></svg>
    <svg viewBox="0 0 14 14" aria-hidden="true"><path d="M7 13S2.5 8 2.5 5.3a4.5 4.5 0 019 0C11.5 8 7 13 7 13z" fill="none" stroke="currentColor" stroke-width="1.5"/><circle cx="7" cy="5.3" r="1.5" fill="currentColor"/></svg>
  </div>
  <div class="roofline-band" role="img" aria-label="Row of house outlines" style="top:239px;"></div>
  <p class="slogan" style="top:328px;">"Leader in quality neighborhood communities"</p>
</section>

</body>
</html>
```